Re-design of website: www.veltramedia.ca/en/

Veltrameda B is a promotional agency specializing in on-site marketing. We are re-designing their website.

We have already produced a prototype:
http://norvapixel.com/veltramedia_siteweb/

The architecture in the prototype must be respected. Please dress up the design with green, grey and black circles and other textures found on their current website www.veltramedia.ca

Inspiration for design that we like, clean, flat design:

- http://www.brimfoxlab.co/
- http://quellarworks.com/#!/process
- http://wearetolvane.com/

Delivrables: PSD files of each page of the prototype

Here are the images of their print portfolio: http://ftp.veltramedia.ca/clients/VLM/VELTRAMEDIA-PORTFOLIO-2012_EN.zip

Industry/Entity Type

Architecture

Requirements
Must have
• Responsive Design

```html
<!DOCTYPE html>
<html lang="fr">
<head>
<meta charset="utf-8">
<title>Veltrameda B — Agence</title>
<link href="https://fonts.googleapis.com/css2?family=Roboto+Condensed:wght@400;700&family=Arimo:wght@400;700&display=swap" rel="stylesheet">
<style>
  :root {
    --green: #9fcb63;
    --green-dark: #5f7d3a;
    --hero-grey: #5f5f5f;
    --band-grey: #dcdcdc;
    --ring-grey: #e9e9e9;
    --disc-grey: #5b5b5b;
    --footer-grey: #575757;
    --ink: #111111;
    --white: #ffffff;
    --link-blue: #3b6fd8;
  }
  * { margin: 0; padding: 0; box-sizing: border-box; }
  html, body { width: 847px; height: 1200px; overflow: hidden; background: var(--white); }
  body { position: relative; font-family: "Arimo", Arial, sans-serif; color: var(--ink); }

  .site-header { position: absolute; top: 0; left: 0; width: 847px; height: 110px; background: var(--white); }
  .brand { position: absolute; top: 34px; left: 0; width: 847px; display: flex; justify-content: center; align-items: center; gap: 12px; }
  .brand-name { font-family: "Roboto Condensed", Arial, sans-serif; font-weight: 700; font-size: 36px; letter-spacing: 3px; color: var(--ink); text-transform: uppercase; }
  .brand-dot { width: 38px; height: 38px; border-radius: 50%; background: var(--green); }

  .main-nav { position: absolute; top: 110px; left: 0; width: 847px; height: 42px; background: var(--green); }
  .nav-links { list-style: none; }
  .nav-links li { position: absolute; top: 15px; font-family: "Roboto Condensed", Arial, sans-serif; font-weight: 700; font-size: 12px; line-height: 14px; color: var(--ink); white-space: nowrap; }
  .nav-links li.is-active { color: var(--white); }
  .nav-agence { left: 64px; }
  .nav-services { left: 137px; }
  .nav-works { left: 218px; }
  .nav-events { left: 323px; }
  .nav-jobs { left: 422px; }
  .nav-contact { left: 532px; }
  .social-links { position: absolute; left: 664px; top: 121px; display: flex; gap: 6px; }
  .social-links span { width: 20px; height: 20px; border-radius: 3px; background: var(--green-dark); border: 1px solid #3f5426; }

  .hero { position: absolute; top: 152px; left: 0; width: 847px; height: 275px; background: var(--hero-grey);
    display: flex; align-items: center; justify-content: center; }
  .hero-text { font-family: "Roboto Condensed", Arial, sans-serif; font-weight: 700; font-size: 30px; line-height: 30px; color: var(--white); text-align: center; white-space: nowrap; }

  .works-title { position: absolute; top: 453px; left: 0; width: 847px; text-align: center; font-family: "Roboto Condensed", Arial, sans-serif; font-weight: 700; font-size: 30px; line-height: 36px; color: var(--green); }
  .works-grid { position: absolute; top: 507px; left: 33px; display: grid; grid-template-columns: repeat(4, 190px); grid-auto-rows: 155px; gap: 7px 8px; }
  .work-tile { width: 190px; height: 155px; }
  .tile-green { background: linear-gradient(160deg, #5fa56c, #4a8f58); }
  .tile-blue { background: linear-gradient(160deg, #3ba3c8, #2b8fb3); }
  .tile-mountain { background: linear-gradient(180deg, #8d9693, #4d5654); }
  .tile-dark { background: linear-gradient(180deg, #2b2b2b, #3c3c3c); }
  .tile-slate { background: linear-gradient(180deg, #8c9299, #a5abb1); }
  .tile-paper { background: linear-gradient(180deg, #e2e2e2, #d6d6d6); }
  .tile-forest { background: linear-gradient(150deg, #3f8a48, #2d2d2d); }
  .tile-wood { background: linear-gradient(180deg, #8b93a1, #a1a8b4); }

  .works-slider { position: absolute; top: 846px; left: 300px; width: 240px; height: 14px; }
  .slider-minus, .slider-plus { position: absolute; top: -1px; font-weight: 700; font-size: 12px; }
  .slider-minus { left: 3px; }
  .slider-plus { left: 226px; }
  .slider-track { position: absolute; left: 14px; top: 2px; width: 205px; height: 10px; border-radius: 5px; background: var(--ink); }
  .slider-thumb { position: absolute; left: 2px; top: 2px; width: 40px; height: 6px; border-radius: 3px; background: var(--green); }

  .info-band { position: absolute; top: 876px; left: 0; width: 847px; height: 294px; background: var(--band-grey); }
  .info-card { position: absolute; top: 0; width: 180px; text-align: center; }
  .info-card h2 { margin-top: 23px; height: 17px; font-family: "Roboto Condensed", Arial, sans-serif; font-weight: 700; font-size: 14.5px; line-height: 17px; color: var(--green); }
  .info-icon { margin: 7px auto 0; width: 152px; height: 152px; border-radius: 50%; background: var(--ring-grey); display: flex; align-items: center; justify-content: center; }
  .info-icon .disc { width: 120px; height: 120px; border-radius: 50%; background: var(--disc-grey); display: flex; align-items: center; justify-content: center; }
  .info-card p { position: absolute; top: 204px; left: -20px; width: 220px; font-size: 9.4px; line-height: 16.3px; color: var(--ink); white-space: nowrap; }
  .card-contact { left: 78px; }
  .card-jobs { left: 335px; }
  .card-follow { left: 588px; }

  .site-footer { position: absolute; top: 1170px; left: 0; width: 847px; height: 30px; background: var(--footer-grey); color: var(--white); font-size: 7.5px; }
  .footer-links { list-style: none; position: absolute; left: 64px; top: 13px; display: flex; gap: 16px; }
  .footer-links li::before { content: "•"; margin-right: 7px; font-size: 5px; vertical-align: middle; }
  .copyright { position: absolute; left: 461px; top: 15px; }
  .copyright .term { color: var(--link-blue); }
</style>
</head>
<body>
  <header class="site-header">
    <div class="brand">
      <span class="brand-name">Veltrameda B</span>
      <span class="brand-dot"></span>
    </div>
  </header>

  <nav class="main-nav">
    <ul class="nav-links">
      <li class="nav-agence is-active">AGENCE</li>
      <li class="nav-services">SERVICES</li>
      <li class="nav-works">RÉALISATIONS</li>
      <li class="nav-events">ÉVÉNEMENTS</li>
      <li class="nav-jobs">RECRUTEMENT</li>
      <li class="nav-contact">CONTACT</li>
    </ul>
  </nav>
  <div class="social-links" aria-label="Réseaux sociaux">
    <span></span><span></span><span></span><span></span><span></span>
  </div>

  <section class="hero">
    <p class="hero-text">Lorem ipsum dolor sit amet,<br>consecteturadipisicing elit,<br>sed do eiusmod tempor incididunt ut labore.</p>
  </section>

  <h1 class="works-title">Nos réalisations 360</h1>
  <div class="works-grid">
    <div class="work-tile tile-green" role="img" aria-label="Projet : affiche verte de design d'interface web"></div>
    <div class="work-tile tile-blue" role="img" aria-label="Projet : affiche typographique bleue de saison"></div>
    <div class="work-tile tile-mountain" role="img" aria-label="Projet : affiche de saison sur paysage de montagne"></div>
    <div class="work-tile tile-dark" role="img" aria-label="Projet : page de site sombre avec menu"></div>
    <div class="work-tile tile-slate" role="img" aria-label="Projet : campagne de dons sur fond gris"></div>
    <div class="work-tile tile-paper" role="img" aria-label="Projet : emblème de club de fitness"></div>
    <div class="work-tile tile-forest" role="img" aria-label="Projet : identité de studio web verte"></div>
    <div class="work-tile tile-wood" role="img" aria-label="Projet : écusson de restaurant sur bois"></div>
  </div>

  <div class="works-slider">
    <span class="slider-minus">-</span>
    <div class="slider-track"><div class="slider-thumb"></div></div>
    <span class="slider-plus">+</span>
  </div>

  <section class="info-band">
    <article class="info-card card-contact">
      <h2>Contact Us</h2>
      <div class="info-icon"><div class="disc">
        <svg width="64" height="74" viewBox="0 0 64 74" aria-hidden="true">
          <text x="32" y="42" text-anchor="middle" font-family="Arimo, Arial, sans-serif" font-weight="700" font-size="50" fill="#fff">@</text>
          <rect x="12" y="50" width="40" height="22" rx="3" fill="#fff"/>
          <rect x="16" y="45" width="32" height="6" rx="3" fill="#fff"/>
          <g fill="#5b5b5b">
            <rect x="21" y="55" width="5" height="4"/><rect x="30" y="55" width="5" height="4"/><rect x="39" y="55" width="5" height="4"/>
            <rect x="21" y="63" width="5" height="4"/><rect x="30" y="63" width="5" height="4"/><rect x="39" y="63" width="5" height="4"/>
          </g>
        </svg>
      </div></div>
      <p>Lorem ipsum dolor sit amet, consectetur<br>adipiscing elit. Duis eros ligula, lacinia<br>quis euismod in, dignissim at neque.<br>Aliquam quis consectetur magna.</p>
    </article>

    <article class="info-card card-jobs">
      <h2>Recrutement.</h2>
      <div class="info-icon"><div class="disc">
        <svg width="70" height="78" viewBox="0 0 70 78" aria-hidden="true">
          <ellipse cx="35" cy="24" rx="16" ry="20" fill="#fff"/>
          <path d="M2 78 C4 58 16 50 35 50 C54 50 66 58 68 78 Z" fill="#fff"/>
        </svg>
      </div></div>
      <p>Lorem ipsum dolor sit amet, consectetur<br>adipiscing elit. Duis eros ligula, lacinia<br>quis euismod in, dignissim at neque.<br>Aliquam quis consectetur magna.</p>
    </article>

    <article class="info-card card-follow">
      <h2>Suivez-nous.</h2>
      <div class="info-icon"><div class="disc">
        <svg width="68" height="68" viewBox="0 0 68 68" aria-hidden="true">
          <rect x="3" y="8" width="62" height="57" rx="5" fill="none" stroke="#fff" stroke-width="6"/>
          <rect x="3" y="8" width="62" height="12" fill="#fff"/>
          <rect x="15" y="1" width="7" height="14" rx="3" fill="#fff"/>
          <rect x="46" y="1" width="7" height="14" rx="3" fill="#fff"/>
          <g fill="#fff">
            <rect x="15" y="28" width="10" height="9"/><rect x="29" y="28" width="10" height="9"/><rect x="43" y="28" width="10" height="9"/>
            <rect x="15" y="42" width="10" height="9"/><rect x="29" y="42" width="10" height="9"/><rect x="43" y="42" width="10" height="9"/>
          </g>
        </svg>
      </div></div>
      <p>Lorem ipsum dolor sit amet, consectetur<br>adipiscing elit. Duis eros ligula, lacinia<br>quis euismod in, dignissim at neque.<br>Aliquam quis consectetur magna.</p>
    </article>
  </section>

  <footer class="site-footer">
    <ul class="footer-links">
      <li>Home</li>
      <li>About us</li>
      <li>Services</li>
      <li>Contact us</li>
    </ul>
    <p class="copyright">Copyright (c) 2013 Veltrameda B.com - <span class="term">Term</span> - Police - All Rights Reserved</p>
  </footer>
</body>
</html>
```